roomnestly.com banner ads

Hi All,

I'm looking for a set of banner ads designing for a Vextra Clickline campaign for roomnestly.com.

The website serves the UK and is a portal for people who cannot afford to buy or rent a place of their own, to find a room to let in someone else's house.

Conversely, home owners can pay to advertise a listing of their spare room. Have a look at the site, and you'll get the idea. Please bear in mind that it's a work in progress and is currently being developed and polished.

The banners do not have to be animated (no Flash please) but should cover all the standard sizes used by Vextra Clickline.

Please take design guidance and inspiration from the web site itself. I'm looking for something eye-catching and creative.

Many thanks,
Colm

Target Market(s)

1. People who can't afford to buy or rent a property

Industry/Entity Type

House

Requirements
Must have
• The logo should be prominent in the ads

```html
<!DOCTYPE html>
<html lang="en">
<head>
<meta charset="utf-8">
<title>roomnestly.com banner – Double room in Fulham</title>
<link rel="stylesheet" href="https://fonts.googleapis.com/css2?family=Arimo:wght@400;700&display=swap">
<style>
  :root {
    --orange: #f07d00;
    --orange-light: #f9a23a;
    --navy: #0b2a5e;
    --ink: #333333;
    --muted: #555555;
    --panel-grey-top: #f4f4f4;
    --panel-grey-bottom: #cfcfcf;
    --button-dark: #111111;
    --button-mid: #3a3a3a;
    --brand-blue: #1f5aa6;
    --room-pink: #c4607e;
    --room-dark: #4a2b33;
    --white: #ffffff;
  }
  * { box-sizing: border-box; margin: 0; padding: 0; }
  html, body { width: 1200px; height: 148px; overflow: hidden; background: var(--white); }
  .banner {
    position: relative;
    width: 1200px; height: 148px;
    font-family: "Arimo", Arial, sans-serif;
    background: var(--white);
    overflow: hidden;
  }
  .room-photo {
    position: absolute; left: 0; top: 0;
    width: 219px; height: 148px;
    background: linear-gradient(135deg, var(--room-pink) 0%, #9a4862 45%, var(--room-dark) 100%);
  }
  .listing-frame {
    position: absolute; left: 219px; top: 0; width: 720px; height: 148px;
  }
  .listing-frame svg { position: absolute; inset: 0; }
  .strapline {
    position: absolute; left: 400px; top: 3px; width: 420px;
    text-align: center; color: var(--white);
    font-size: 15px; font-weight: 700;
  }
  .listing {
    position: absolute; left: 272px; top: 32px; width: 640px;
  }
  .listing-title {
    color: var(--orange); font-size: 24px; font-weight: 700; line-height: 30px;
  }
  .listing-excerpt {
    margin-top: 10px; color: var(--ink); font-size: 18px; line-height: 24px;
  }
  .more-link { color: var(--orange); font-size: 18px; text-decoration: none; line-height: 24px; }
  .listing-price {
    position: absolute; left: 625px; top: 108px;
    color: var(--muted); font-size: 20px;
  }
  .cta-panel {
    position: absolute; left: 925px; top: 0; width: 275px; height: 148px;
    background: linear-gradient(180deg, var(--panel-grey-top), var(--panel-grey-bottom));
  }
  .cta-button {
    position: absolute; left: 10px; top: 10px; width: 255px; height: 68px;
    border-radius: 10px;
    background: linear-gradient(180deg, var(--button-mid), var(--button-dark));
    display: flex; align-items: center; padding-left: 22px; gap: 16px;
    color: var(--white); font-size: 24px; font-weight: 700; text-decoration: none;
  }
  .cta-arrow { width: 38px; height: 38px; }
  .brand {
    position: absolute; left: 18px; top: 98px;
    display: flex; align-items: center; gap: 8px;
  }
  .brand-mark { width: 26px; height: 26px; background: var(--brand-blue); }
  .brand-name { color: var(--brand-blue); font-size: 28px; font-weight: 700; letter-spacing: -0.5px; }
</style>
</head>
<body>
<div class="banner">
  <div class="room-photo" role="img" aria-label="Photo of the double room for rent: pink walls, white chest of drawers and a bed"></div>

  <div class="listing-frame">
    <svg width="720" height="148" viewBox="0 0 720 148" aria-hidden="true">
      <rect x="0" y="0" width="720" height="24" fill="var(--orange)"/>
      <path d="M175 0 H620 L605 22 H190 Z" fill="var(--navy)"/>
      <path d="M700 30 H40 Q18 30 18 52 V118 Q18 140 40 140 H706" fill="none" stroke="var(--orange)" stroke-width="4"/>
      <path d="M0 24 H720" stroke="var(--orange-light)" stroke-width="2"/>
    </svg>
  </div>

  <div class="strapline">Latest rooms in and around London</div>

  <div class="listing">
    <h1 class="listing-title">Double Room available for rent in Fulham</h1>
    <p class="listing-excerpt">Hi, after over 2 years in this great flat, I'm moving out to</p>
    <a class="more-link" href="#">More...</a>
  </div>
  <div class="listing-price">US$330, Double room</div>

  <div class="cta-panel">
    <a class="cta-button" href="#">
      Find Out More
      <svg class="cta-arrow" viewBox="0 0 38 38" aria-hidden="true">
        <circle cx="19" cy="19" r="18" fill="var(--white)"/>
        <path d="M15 11 L26 19 L15 27 Z" fill="var(--button-dark)"/>
      </svg>
    </a>
    <div class="brand">
      <span class="brand-mark"></span>
      <span class="brand-name">roomnestly.com</span>
    </div>
  </div>
</div>
</body>
</html>
```